Buch-/eBook-Cover für Traumatherapeutin
Zielgruppe
Ich bin Traumatherapeutin und schreibe ein Buch zum Thema Trauma bearbeiten.
Meine Zielgruppe sucht Heilung, Genesung, Selbstliebe etc.
Aufgabenstellung
Buchcover
Bitte erstell mir ein modernes positives inspirierendes Buchcover mit dem
Titel: 'Morgens LEISE aufbrechen“
Untertitel: „Geh den Pfad, der dich leise ruft“
Dr. Merle Kuhnast
Ich hätte gerne ein modernes Buch, das entweder einen Bezug zum Thema Trauma hat oder aber einfach stylische Schriftzüge. Bin aber auch offen für andere Vorschläge.
Dunkelblau, weiß und türkis oder auch rosa mag ich ganz gerne. Wobei Dunkelblau, weiß und türkis meine Favoriten sind und mit rosa höchstens kleinere Akzente gesetzt werden sollten.
Das Buchcover soll modern sein und direkt ansprechen. Gerne eine originelle Lösung, oder etwas Besonderes, etwas das Tiefe ausdrückt, oder man mehrmals hinsehen muss um etwas zu erkennen oder etwas das mehr Interpretationsspielraum lässt.
Gerne auch viel weiß, zumindest heller und nicht zu dunkel. Stylish, aber nicht überfrachtet.
Schreib mich gerne an, wenn du Fragen hast.
Ich habe mal zwei Beispiel von Typolösungen angehängt, die ich ganz cool fände.
Ich freue mich auf deine Ideen :-)
Ganz liebe Grüße
Merle

```html
<!DOCTYPE html>
<html lang="de">
<head>
<meta charset="utf-8">
<title>Morgens LEISE aufbrechen – Dr. Merle Kuhnast</title>
<link rel="stylesheet" href="https://fonts.googleapis.com/css2?family=Montserrat:ital,wght@0,700;0,800;1,400&family=Sacramento&display=swap">
<style>
  :root {
    --bg-top: #5b4b96;
    --bg-mid: #443f85;
    --bg-bottom: #2c2d62;
    --glow: rgba(124, 138, 206, 0.42);
    --glow-edge: rgba(124, 138, 206, 0);
    --white: #ffffff;
    --rose: #e8a2ca;
  }
  html, body {
    margin: 0;
    padding: 0;
    overflow: hidden;
    background: var(--bg-bottom);
  }
  .cover {
    position: relative;
    width: 858px;
    height: 1200px;
    overflow: hidden;
    background: linear-gradient(180deg, var(--bg-top) 0%, var(--bg-mid) 48%, var(--bg-bottom) 100%);
    font-family: "Montserrat", sans-serif;
    color: var(--white);
  }
  .author {
    position: absolute;
    top: 70px;
    left: 0;
    width: 100%;
    margin: 0;
    text-align: center;
    font-weight: 700;
    font-size: 44px;
    line-height: 1;
  }
  .word-cloud-area {
    position: absolute;
    left: 20px;
    top: 320px;
    width: 818px;
    height: 640px;
    background: radial-gradient(ellipse 50% 50% at 50% 50%, var(--glow) 0%, var(--glow) 35%, var(--glow-edge) 100%);
  }
  .title {
    margin: 0;
    font-weight: normal;
  }
  .title-script {
    position: absolute;
    font-family: "Sacramento", cursive;
    color: var(--rose);
    font-size: 100px;
    line-height: 1;
    white-space: nowrap;
  }
  .title-script--top {
    left: 100px;
    top: 404px;
  }
  .title-script--bottom {
    right: 98px;
    top: 598px;
  }
  .title-main {
    position: absolute;
    left: 0;
    width: 100%;
    top: 500px;
    text-align: center;
    font-weight: 800;
    font-size: 112px;
    line-height: 1;
    letter-spacing: 4px;
    color: var(--white);
  }
  .subtitle {
    position: absolute;
    right: 132px;
    top: 712px;
    margin: 0;
    font-style: italic;
    font-weight: 400;
    font-size: 28px;
    line-height: 1.2;
    text-align: right;
  }
</style>
</head>
<body>
  <main class="cover">
    <p class="author">Dr. Merle Kuhnast</p>

    <div class="word-cloud-area" role="img" aria-label="Wortwolke mit Begriffen rund um Trauma in Gehirnform"></div>

    <h1 class="title">
      <span class="title-script title-script--top">Morgens</span>
      <span class="title-main">LEISE</span>
      <span class="title-script title-script--bottom">aufbrechen</span>
    </h1>

    <p class="subtitle">Geh den Pfad,<br>der dich leise ruft</p>
  </main>
</body>
</html>
```